Apply Existing Website Design to Pellmoor-Made Tele-Wellness App (UX/UI Work)

We’re looking for a highly skilled UX/UI designer to translate our existing website design into an intuitive, beautiful mobile app interface for our Pellmoor-developed tele-wellness platform. Hoping this designer will stay onboard with us for future work.

Scope of Work:
    •    Review our existing website design (style, colors, typography, components)
    •    Apply the same visual language to our mobile app screens
    •    Ensure consistent, user-friendly experience across the app
    •    Deliver high-fidelity mockups and design assets (preferably in Figma)
    •    Minimal UX rethinking may be needed to optimize for mobile, but the core brand and design system are already established

What We Provide:
    •    Access to the existing website design (including any style guides or component libraries)
    •    Wireframes or a basic functional map of the app screens
    •    Clear guidelines on branding and user flows

Ideal Candidate:
    •    Strong portfolio of mobile app design, especially healthcare/wellness preferred
    •    Proven experience in adapting web designs for mobile apps
    •    Expertise with Figma or comparable tools
    •    Attention to detail and commitment to brand consistency
    •    Ability to deliver quickly while maintaining quality

Deliverables:
    •    Complete set of high-fidelity, mobile-optimized app screens
    •    Organized design file (Figma preferred) ready for developer handoff
    •    Design assets as needed (icons, images, components)

Timeline:
    •    Estimated 1 week for initial delivery, with room for revisions

```html
<!DOCTYPE html>
<html lang="en">
<head>
<meta charset="utf-8">
<title>Kinora Tele-Wellness App Screens</title>
<link rel="stylesheet" href="https://fonts.googleapis.com/css2?family=Lora:wght@600;700&family=Plus+Jakarta+Sans:wght@400;500;600;700;800&display=swap">
<style>
:root{
  --canvas:#f7f7f7;
  --white:#ffffff;
  --peach:#fdcb9b;
  --peach-soft:#fde6d0;
  --orange:#f4a259;
  --orange-deep:#e98a35;
  --ink:#1f2426;
  --muted:#8a8f93;
  --line:#eeeeee;
  --green:#2f6e3b;
  --green-bright:#5fc34d;
  --red:#f2455b;
  --blue:#3f86f4;
  --yellow:#f6c33a;
  --dark:#2d3436;
  --star:#f5b623;
}
*{box-sizing:border-box;margin:0;padding:0}
html,body{width:1200px;height:661px;overflow:hidden;background:var(--canvas)}
body{position:relative;font-family:"Plus Jakarta Sans",sans-serif;color:var(--ink)}
.screen{position:absolute;width:97px;background:var(--white);border-radius:9px;overflow:hidden;box-shadow:0 2px 8px rgba(0,0,0,.05)}
.screen > *{position:absolute}
.status{top:4px;left:8px;font-size:3.6px;font-weight:700}
.status-icons{top:4.5px;right:8px;width:12px;height:3px;background:linear-gradient(90deg,var(--ink) 0 30%,transparent 30% 40%,var(--ink) 40% 60%,transparent 60% 70%,var(--ink) 70%);border-radius:1px}
.home-bar{bottom:3px;left:50%;width:34px;height:1.3px;margin-left:-17px;background:var(--ink);border-radius:1px}
.h{font-family:"Lora",serif;font-weight:700}
.sec{font-family:"Lora",serif;font-weight:700;font-size:4px;left:2px}
.see{font-size:3px;color:var(--muted);right:4px}
.tiny{font-size:2.8px;color:var(--muted)}
.card{background:var(--white);border-radius:4px;box-shadow:0 0 0 .4px var(--line),0 1px 3px rgba(0,0,0,.04)}
.photo{background:linear-gradient(160deg,#e9e4df,#cfc8c2 60%,#b9b2ac);border-radius:3px}
.avatar{width:12px;height:12px;border-radius:3px;background:linear-gradient(150deg,#e6e0da,#bfb6ae)}
.name{font-size:3.8px;font-weight:700}
.meta{font-size:2.8px;color:var(--muted)}
.stars{color:var(--star);font-size:3.2px;letter-spacing:-.2px}
.tick{display:inline-block;width:3.6px;height:3.6px;border-radius:50%;background:var(--green-bright);vertical-align:middle}
.nav{height:18px;background:var(--dark);border-radius:6px;display:flex;align-items:center;justify-content:space-around;padding:0 4px}
.nav i{display:block;width:3.6px;height:3.6px;border-radius:1px;background:#9aa2a4}
.nav i.on{width:8px;height:8px;border-radius:3px;background:var(--white)}
.back{width:9px;height:9px;border-radius:3px;background:#f2f2f2;font-size:5px;line-height:9px;text-align:center}
.topbar-title{font-family:"Lora",serif;font-weight:700;font-size:4.6px}
.btn-orange{background:var(--peach);color:var(--orange-deep);font-weight:700;border-radius:3px;text-align:center}
.chip{display:inline-block;font-size:2.8px;padding:1px 2px;border-radius:2px;background:#f7f7f7;margin:0 1px 1px 0}
.row{display:flex;justify-content:space-between}
</style>
</head>
<body>

<!-- Splash -->
<section class="screen splash" style="left:18px;top:36px;height:210px;background:var(--peach)">
  <div class="status" style="color:#fff">9:41</div>
  <div class="brand" style="top:91px;left:0;width:97px;text-align:center;font-size:17px;font-weight:800;color:#fff;letter-spacing:.5px">KINORA</div>
  <div class="h" style="top:115px;left:0;width:97px;text-align:center;font-size:4.4px;line-height:7.5px;color:#e59b5c;font-weight:600">Holistic-Doctor led care<br>Pay as you like</div>
  <div class="home-bar" style="background:#fff"></div>
</section>

<!-- Splash alt -->
<section class="screen splash" style="left:18px;top:277px;height:210px">
  <div class="brand" style="top:88px;left:0;width:97px;text-align:center;font-size:17px;font-weight:800;color:var(--peach);letter-spacing:.5px">KINORA</div>
  <div class="h" style="top:112px;left:0;width:97px;text-align:center;font-size:4.4px;line-height:7.5px;color:var(--orange);font-weight:600">Holistic-Doctor led care<br>Pay as you like</div>
</section>

<!-- Welcome -->
<section class="screen welcome" style="left:135px;top:36px;height:210px">
  <div class="status">9:41</div><div class="status-icons"></div>
  <div style="top:38px;left:0;width:97px;text-align:center;font-size:6.5px;font-weight:800;color:var(--peach)">KINORA</div>
  <div class="h" style="top:50px;left:4px;width:89px;text-align:center;font-size:7.6px;line-height:9.6px">Welcome to the <span style="color:var(--peach)">Kinora</span><br>Tele-Wellness!</div>
  <div style="top:75px;left:0;width:97px;text-align:center;font-size:4.4px;color:var(--muted)">Evidence based care with heart</div>
  <div role="img" aria-label="Three smiling doctors in scrubs and white coats" style="top:100px;left:12px;width:73px;height:84px;border-radius:8px;background:linear-gradient(180deg,#f7f3ef,#e8eef0 60%,#d7e3e6)"></div>
  <div class="btn-orange" style="top:153px;left:24px;width:48px;height:14px;line-height:14px;font-size:4.4px">Get Started →</div>
  <div style="top:172px;left:0;width:97px;text-align:center;font-size:3.3px;color:var(--muted)">Already have an account? <span style="color:var(--orange)">Sign In</span></div>
  <div class="home-bar"></div>
</section>

<!-- Home dashboard -->
<section class="screen home" style="left:252px;top:36px;height:591px">
  <div class="status">9:41</div><div class="status-icons"></div>
  <div style="top:17px;left:4px;font-size:2.9px;font-weight:700;color:var(--muted)">▣ SAT, 25 JUN 2026</div>
  <div style="top:17px;right:5px;width:4px;height:4px;border-radius:50%;background:var(--red)"></div>
  <div class="avatar" role="img" aria-label="User portrait" style="top:25px;left:4px;width:13px;height:13px;border-radius:50%"></div>
  <div style="top:26px;left:20px;font-size:5.5px;font-weight:800">Hello, Elsa!</div>
  <div style="top:34px;left:20px;font-size:2.9px;color:var(--muted)"><span style="color:var(--green-bright)">✚</span> 94% Healthy · <span style="color:var(--star)">★</span> Pro Member</div>
  <div style="top:28px;right:5px;font-size:5px">›</div>
  <div class="sec" style="top:56px">Quick Health Summary</div>
  <div class="card" style="top:65px;left:2px;width:40px;height:51px;background:var(--green);border-radius:5px">
    <div style="position:absolute;top:4px;left:4px;font-size:3px;font-weight:700;color:#fff">Heart Rate</div>
    <div style="position:absolute;top:10px;left:4px;font-size:6px;font-weight:800;color:#fff">96 <span style="font-size:3px">bpm</span></div>
    <svg style="position:absolute;top:22px;left:2px" width="36" height="26" viewBox="0 0 36 26"><path d="M1 24 C6 10,8 8,11 20 S16 2,19 14 S24 20,27 6 S32 10,35 4" fill="none" stroke="#7ed957" stroke-width="1.6"/></svg>
  </div>
  <div class="card" style="top:65px;left:45px;width:40px;height:51px;background:var(--red);border-radius:5px">
    <div style="position:absolute;top:4px;left:4px;font-size:3px;font-weight:700;color:#fff">Steps Taken</div>
    <div style="position:absolute;top:10px;left:4px;font-size:6px;font-weight:800;color:#fff">1578 <span style="font-size:3px">total</span></div>
    <svg style="position:absolute;top:22px;left:4px" width="32" height="26" viewBox="0 0 32 26"><g fill="#ff9aa6"><rect x="1" y="16" width="3" height="10" rx="1.5"/><rect x="6" y="10" width="3" height="16" rx="1.5"/><rect x="11" y="4" width="3" height="22" rx="1.5" fill="#fff"/><rect x="16" y="12" width="3" height="14" rx="1.5"/><rect x="21" y="18" width="3" height="8" rx="1.5"/><rect x="26" y="21" width="3" height="5" rx="1.5"/></g></svg>
  </div>
  <div style="top:65px;left:88px;width:12px;height:51px;background:var(--blue);border-radius:5px"></div>
  <div style="top:122px;left:40px;width:16px;height:1.6px;background:radial-gradient(circle,var(--ink) 40%,transparent 45%) 0 0/4px 1.6px"></div>
  <div class="sec" style="top:133px">Virtual Consultations</div>
  <div class="card" style="top:143px;left:2px;width:89px;height:93px">
    <div style="position:absolute;top:5px;left:5px;font-size:9px;font-weight:800">89+</div>
    <div style="position:absolute;top:16px;left:5px;font-size:3px;color:var(--muted)">List Consultations</div>
    <div style="position:absolute;top:6px;right:4px;width:9px;height:9px;border:.5px solid #ddd;border-radius:2px;text-align:center;line-height:8.5px;font-size:6px;color:var(--muted)">+</div>
    <div style="position:absolute;top:25px;left:4px;width:81px;height:23px;background:#f8f8f8;border-radius:3px">
      <div class="avatar" role="img" aria-label="Doctor portrait" style="position:absolute;top:4px;left:3px;width:14px;height:15px"></div>
      <div class="name" style="position:absolute;top:4px;left:20px">Dr. Clara Voss</div>
      <div class="meta" style="position:absolute;top:10px;left:20px"><span class="stars">★</span> 4.1 · Cardiologist</div>
      <div class="meta" style="position:absolute;top:15px;left:20px">● 15:25 PM - 17:25 PM</div>
    </div>
    <div style="position:absolute;top:51px;left:4px;width:81px;height:23px;background:#f8f8f8;border-radius:3px">
      <div class="avatar" role="img" aria-label="Doctor portrait" style="position:absolute;top:4px;left:3px;width:14px;height:15px"></div>
      <div class="name" style="position:absolute;top:4px;left:20px">Dr. Owen Hale</div>
      <div class="meta" style="position:absolute;top:10px;left:20px"><span class="stars">★</span> 4.6 · Orthopedics</div>
      <div class="meta" style="position:absolute;top:15px;left:20px">● 9:25 AM - 11:25 AM</div>
    </div>
    <div style="position:absolute;top:79px;left:35px;width:21px;height:7px;background:var(--dark);color:#fff;border-radius:3px;font-size:2.8px;line-height:7px;text-align:center">See All →</div>
  </div>
  <div class="sec" style="top:246px">Medication Management</div>
  <div style="top:254px;left:2px;width:89px;height:70px;background:var(--peach);border-radius:5px">
    <div style="position:absolute;top:5px;left:4px;font-size:9px;font-weight:800;color:var(--orange-deep)">146+</div>
    <div style="position:absolute;top:16px;left:4px;font-size:3px;color:#fff">Total Medications</div>
    <div style="position:absolute;top:6px;right:4px;width:9px;height:9px;border:.5px solid #fff;border-radius:2px;color:#fff;text-align:center;line-height:8.5px;font-size:6px">+</div>
    <div style="position:absolute;top:25px;left:4px;width:39px;height:31px;background:#fff;border-radius:3px">
      <div style="position:absolute;top:4px;left:4px;width:8px;height:8px;border-radius:50%;background:#fde2e5"></div>
      <div class="name" style="position:absolute;top:16px;left:3px;font-size:3.3px">Amoxicillin</div>
      <div class="meta" style="position:absolute;top:22px;left:3px">250mcg · Before Eat</div>
    </div>
    <div style="position:absolute;top:25px;left:47px;width:39px;height:31px;background:#fff;border-radius:3px">
      <div style="position:absolute;top:4px;left:4px;width:8px;height:8px;border-radius:50%;background:#ece4fb"></div>
      <div class="name" style="position:absolute;top:16px;left:3px;font-size:3.3px">Ranitidine</div>
      <div class="meta" style="position:absolute;top:22px;left:3px">150mcg · After Eat</div>
    </div>
    <div style="position:absolute;top:61px;left:4px;font-size:3px;color:var(--orange-deep);font-weight:600">4 Needs Refill</div>
    <div style="position:absolute;top:59px;right:4px;width:20px;height:7px;background:var(--dark);color:#fff;border-radius:3px;font-size:2.8px;line-height:7px;text-align:center">See All →</div>
  </div>
  <div class="sec" style="top:336px">Symptom Checker</div>
  <div class="card" style="top:344px;left:2px;width:89px;height:53px">
    <div style="position:absolute;top:5px;left:5px;font-size:9px;font-weight:800">16</div>
    <div style="position:absolute;top:16px;left:5px;font-size:3px;color:var(--muted)">Active Symptoms</div>
    <div style="position:absolute;top:6px;right:4px;width:9px;height:9px;border:.5px solid #ddd;border-radius:2px;text-align:center;line-height:8.5px;font-size:6px;color:var(--muted)">+</div>
    <div style="position:absolute;top:25px;left:4px;width:81px;height:10px;background:#f5f5f5;border-radius:3px;font-size:3px;line-height:10px;padding-left:4px">Search symptoms...</div>
    <div style="position:absolute;top:40px;left:4px;font-size:2.7px"><b>Most Common</b> <span class="chip">Fever ×</span><span class="chip">Alergic ×</span><span class="chip">Vague ×</span></div>
  </div>
  <div class="sec" style="top:405px">E-Pharmacy</div><div class="see" style="top:406px">See All</div>
  <div class="card" style="top:413px;left:2px;width:38px;height:58px">
    <div role="img" aria-label="Amoxicillin medicine box" class="photo" style="position:absolute;top:3px;left:3px;width:32px;height:32px;background:linear-gradient(160deg,#eef3f6,#c9d7de)"></div>
    <div style="position:absolute;top:38px;left:3px;font-size:3.2px">Amoxicillin</div>
    <div style="position:absolute;top:46px;left:3px;font-size:3.6px;font-weight:800">$9.99</div>
    <div style="position:absolute;top:44px;right:3px;width:8px;height:8px;border-radius:2px;background:var(--peach);color:#fff;text-align:center;line-height:8px;font-size:6px">+</div>
  </div>
  <div class="card" style="top:413px;left:43px;width:38px;height:58px">
    <div role="img" aria-label="Ranitidine tablets in blister pack" class="photo" style="position:absolute;top:3px;left:3px;width:32px;height:32px;background:linear-gradient(160deg,#eef3f0,#bcd0c6)"></div>
    <div style="position:absolute;top:38px;left:3px;font-size:3.2px">Ranitidine</div>
    <div style="position:absolute;top:46px;left:3px;font-size:3.6px;font-weight:800">$7.99</div>
    <div style="position:absolute;top:44px;right:3px;width:8px;height:8px;border-radius:2px;background:var(--peach);color:#fff;text-align:center;line-height:8px;font-size:6px">+</div>
  </div>
  <div class="card" style="top:413px;left:84px;width:20px;height:58px">
    <div role="img" aria-label="Paracetamol box" style="position:absolute;top:3px;left:3px;width:20px;height:32px;background:linear-gradient(160deg,#fbe9a8,#f3c64a);border-radius:3px"></div>
    <div style="position:absolute;top:38px;left:3px;font-size:3.2px">Parac</div>
    <div style="position:absolute;top:46px;left:3px;font-size:3.6px;font-weight:800">$9.9</div>
  </div>
  <div class="sec" style="top:477px">Resources &amp; Workshop</div><div class="see" style="top:478px">See All</div>
  <div class="card" style="top:485px;left:2px;width:80px;height:61px">
    <div role="img" aria-label="Stethoscope resting on a medical chart" style="position:absolute;top:2px;left:2px;width:76px;height:44px;border-radius:3px;background:linear-gradient(160deg,#f1f3f5,#c9d0d6)"></div>
    <div style="position:absolute;top:49px;left:3px;font-size:3.6px;font-weight:600;line-height:4.6px">Cardio Monitoring with<br>mobile App 2025</div>
    <div style="position:absolute;top:50px;right:3px;width:8px;height:8px;border-radius:2px;background:#f3f3f3;font-size:4px;text-align:center;line-height:8px">→</div>
  </div>
  <div class="card" style="top:485px;left:84px;width:20px;height:61px">
    <div role="img" aria-label="Wellness workshop scene" style="position:absolute;top:2px;left:2px;width:18px;height:44px;border-radius:3px;background:linear-gradient(160deg,#e4eaef,#b9c4cc)"></div>
    <div style="position:absolute;top:49px;left:3px;font-size:3.6px;font-weight:600;line-height:4.6px">Well<br>Conf</div>
  </div>
  <div style="top:555px;left:40px;width:16px;height:1.6px;background:radial-gradient(circle,var(--ink) 40%,transparent 45%) 0 0/4px 1.6px"></div>
  <div class="nav" style="top:567px;left:4px;width:89px"><i class="on"></i><i></i><i></i><i></i><i></i></div>
</section>

<!-- Doctor detail -->
<section class="screen detail" style="left:369px;top:36px;height:523px">
  <div role="img" aria-label="Portrait of Dr. Lena Marsh in white coat with stethoscope" style="top:0;left:0;width:97px;height:88px;background:linear-gradient(170deg,#eceae8,#cfc9c5 55%,#b8b0aa)"></div>
  <div class="status" style="color:#fff">9:41</div>
  <div class="back" style="top:16px;left:5px;background:#fff">‹</div>
  <div class="h" style="top:18px;left:0;width:97px;text-align:center;font-size:4.6px;color:#fff">Doctor Detail</div>
  <div class="back" style="top:16px;right:5px;background:#fff;left:auto">⚙</div>
  <div class="card" style="top:81px;left:4px;width:89px;height:24px">
    <div style="position:absolute;top:4px;left:0;width:89px;text-align:center;font-size:5.8px;font-weight:700">Dr. Lena Marsh <span class="tick" style="width:5px;height:5px"></span></div>
    <div style="position:absolute;top:15px;left:0;width:89px;text-align:center;font-size:3.3px"><span class="stars">★</span> 4.5 &nbsp; ◉ 501m &nbsp; <span style="color:var(--green-bright)">✦</span> Neurologist</div>
  </div>
  <div style="top:113px;left:4px;width:89px;height:11px;background:#f2f2f2;border-radius:4px">
    <div style="position:absolute;top:1px;left:1px;width:43px;height:9px;background:#fff;border-radius:3px;font-size:3.2px;font-weight:700;text-align:center;line-height:9px">Information</div>
    <div style="position:absolute;top:1px;right:1px;width:43px;height:9px;font-size:3.2px;color:var(--muted);text-align:center;line-height:9px">Availability</div>
  </div>
  <div class="row" style="top:131px;left:4px;width:89px;text-align:center">
    <div style="flex:1"><div style="font-size:6px;font-weight:800">87%</div><div class="tiny">AI Match</div></div>
    <div style="flex:1;border-left:.5px solid var(--line);border-right:.5px solid var(--line)"><div style="font-size:6px;font-weight:800">$25</div><div class="tiny">Booking Cost</div></div>
    <div style="flex:1"><div style="font-size:6px;font-weight:800">48</div><div class="tiny">Awards</div></div>
  </div>
  <div class="sec" style="top:160px;left:4px">Personal Bio</div>
  <div class="tiny" style="top:169px;left:4px;width:89px;line-height:5.6px">Dr. Marsh is a dedicated and compassionate medical professional with a strong commitment to patient care. With years of experience in Orthopedic, she combines expertise and empathy to provide comprehensive healthcare.</div>
  <div class="card" style="top:204px;left:4px;width:89px;height:19px">
    <div style="position:absolute;top:4px;left:3px;width:11px;height:11px;border-radius:3px;background:var(--peach-soft)"></div>
    <div style="position:absolute;top:4px;left:18px;font-size:3.6px;font-weight:700">Earliest Availability</div>
    <div class="meta" style="position:absolute;top:10px;left:18px">Aug 23, 2025 · 10:00 - 12:00</div>
    <div style="position:absolute;top:5px;right:4px;font-size:5px">›</div>
  </div>
  <div class="sec" style="top:231px;left:4px">Visitation History</div><div class="see" style="top:232px">See All</div>
  <div class="card" style="top:240px;left:4px;width:89px;height:29px">
    <div style="position:absolute;top:4px;left:4px;font-size:3.3px"><span style="color:var(--red)">✚</span> Regular Checkup</div>
    <div style="position:absolute;top:3px;right:4px;font-size:2.8px;border:.4px solid #ddd;border-radius:2px;padding:.5px 2px">January ⌄</div>
    <svg style="position:absolute;top:13px;left:4px" width="81" height="5" viewBox="0 0 81 5"><line x1="1" y1="2.5" x2="80" y2="2.5" stroke="#ddd" stroke-width=".6"/><line x1="1" y1="2.5" x2="44" y2="2.5" stroke="#333" stroke-width=".8"/><circle cx="1.5" cy="2.5" r="1.4" fill="#333"/><circle cx="20" cy="2.5" r="1.4" fill="#333"/><circle cx="44" cy="2.5" r="2" fill="#333"/><circle cx="64" cy="2.5" r="1.2" fill="#ccc"/><circle cx="79" cy="2.5" r="1.2" fill="#ccc"/></svg>
    <div class="tiny" style="position:absolute;top:21px;left:4px">Jan 25</div>
    <div style="position:absolute;top:21px;left:39px;font-size:2.8px;font-weight:700">Jan 28</div>
    <div class="tiny" style="position:absolute;top:21px;right:4px">Jan 31</div>
  </div>
  <div class="sec" style="top:279px;left:4px">Specialization <span style="color:var(--muted);font-weight:400">(7)</span></div>
  <div style="top:287px;left:4px;width:91px;font-size:3px;line-height:6px">
    <span class="chip" style="background:none"><span style="color:var(--red)">♥</span> Heart</span><span class="chip" style="background:none"><span style="color:var(--blue)">✢</span> Cardiology</span><span class="chip" style="background:none"><span style="color:#8b5cf6">✦</span> Neurology</span><br>
    <span class="chip" style="background:none"><span style="color:var(--orange)">●</span> Anger</span><span class="chip" style="background:none">◎ Lung</span><span class="chip" style="background:none"><span style="color:var(--green-bright)">●</span> Pediatrics</span>
  </div>
  <div class="sec" style="top:314px;left:4px">Experience</div>
  <div style="top:323px;left:4px;width:89px">
    <div style="position:absolute;left:2px;top:2px;width:.5px;height:58px;background:var(--peach)"></div>
    <div style="position:relative;padding-left:9px;margin-bottom:3.6px"><span style="position:absolute;left:0;top:0;width:5px;height:5px;border-radius:50%;background:var(--peach)"></span><div style="font-size:3.5px;font-weight:700">Fernside Care Center</div><div class="tiny" style="line-height:4.6px">Explore the doctor's clinical excellence and specialized skills honed through experience</div></div>
    <div style="position:relative;padding-left:9px;margin-bottom:3.6px"><span style="position:absolute;left:0;top:0;width:5px;height:5px;border-radius:50%;background:var(--peach)"></span><div style="font-size:3.5px;font-weight:700">Harbor Hospital</div><div class="tiny" style="line-height:4.6px">Observe the tablet's effects on your pain symptoms. While our formula works swiftly.</div></div>
    <div style="position:relative;padding-left:9px;margin-bottom:3.6px"><span style="position:absolute;left:0;top:0;width:5px;height:5px;border-radius:50%;background:var(--orange)"></span><div style="font-size:3.5px;font-weight:700">Calmwell Medical Center</div><div class="tiny" style="line-height:4.6px">Witness the doctor's seamless teamwork and coordination within multidisciplinary.</div></div>
    <div style="position:relative;padding-left:9px"><span style="position:absolute;left:0;top:0;width:5px;height:5px;border-radius:50%;border:.5px solid #ccc;background:#fff"></span><div style="font-size:3.5px;font-weight:700">Northgate Hospital</div><div class="tiny" style="line-height:4.6px">Learn about the doctor's leadership and administrative roles at Harbor Health System.</div></div>
  </div>
  <div class="sec" style="top:404px;left:4px">Gallery <span style="color:var(--muted);font-weight:400">(25)</span></div><div class="see" style="top:405px">See All</div>
  <div role="img" aria-label="Gallery photos of clinic equipment, pills and doctor" style="top:412px;left:4px;width:95px;height:25px;background:repeating-linear-gradient(90deg,#d9d6d3 0 25px,transparent 25px 28px);border-radius:3px"></div>
  <div class="sec" style="top:445px;left:4px">Rating</div><div class="see" style="top:446px">See All</div>
  <div class="card" style="top:452px;left:4px;width:89px;height:31px">
    <div style="position:absolute;top:4px;left:5px;font-size:14px;font-weight:800">4.8</div>
    <div class="tiny" style="position:absolute;top:22px;left:6px">87 Reviews</div>
    <svg style="position:absolute;top:5px;left:36px" width="48" height="22" viewBox="0 0 48 22"><g stroke="#eee" stroke-width="1"><line x1="8" y1="2" x2="47" y2="2"/><line x1="8" y1="6.5" x2="47" y2="6.5"/><line x1="8" y1="11" x2="47" y2="11"/><line x1="8" y1="15.5" x2="47" y2="15.5"/><line x1="8" y1="20" x2="47" y2="20"/></g><g stroke="#2d3436" stroke-width="1"><line x1="8" y1="2" x2="40" y2="2"/><line x1="8" y1="6.5" x2="26" y2="6.5"/><line x1="8" y1="11" x2="30" y2="11"/><line x1="8" y1="15.5" x2="16" y2="15.5"/><line x1="8" y1="20" x2="11" y2="20"/></g><g fill="#f5b623"><circle cx="4" cy="2" r="1"/><circle cx="4" cy="6.5" r="1"/><circle cx="4" cy="11" r="1"/><circle cx="4" cy="15.5" r="1"/><circle cx="4" cy="20" r="1"/></g></svg>
  </div>
  <div style="top:489px;left:4px;width:89px;height:19px;background:var(--dark);border-radius:5px">
    <div style="position:absolute;top:4px;left:4px;font-size:6px;font-weight:800;color:#fff">$97.99</div>
    <div style="position:absolute;top:12px;left:4px;font-size:2.8px;color:#ccc">Consultation Fee</div>
    <div class="btn-orange" style="position:absolute;top:4px;right:3px;width:26px;height:11px;line-height:11px;font-size:3.4px">Book ▣</div>
  </div>
  <div class="home-bar"></div>
</section>

<!-- Browse doctors -->
<section class="screen browse" style="left:487px;top:36px;height:313px">
  <div class="status">9:41</div><div class="status-icons"></div>
  <div class="back" style="top:16px;left:4px">‹</div>
  <div class="topbar-title" style="top:19px;left:19px">Browse All Doctors</div>
  <div class="sec" style="top:36px;left:4px;font-size:3.6px">Browse by Specializations</div><div class="see" style="top:37px">See All</div>
  <div style="top:44px;left:4px;display:flex;gap:3px;font-size:3px;text-align:center;color:var(--muted)">
    <div><div style="width:17px;height:17px;border-radius:4px;background:var(--green)"></div>Heart</div>
    <div><div style="width:17px;height:17px;border-radius:4px;background:var(--green-bright)"></div>Bone</div>
    <div><div style="width:17px;height:17px;border-radius:4px;background:var(--red)"></div>Nutrition</div>
    <div><div style="width:17px;height:17px;border-radius:4px;background:var(--yellow)"></div>Tooth</div>
    <div><div style="width:17px;height:17px;border-radius:4px;background:var(--blue)"></div>Disea</div>
  </div>
  <div class="sec" style="top:77px;left:4px;font-size:3.6px">Lumen AI Recommendation</div>
  <div class="card" style="top:86px;left:4px;width:89px;height:51px">
    <div role="img" aria-label="Doctor portrait" class="photo" style="position:absolute;top:4px;left:4px;width:25px;height:34px"></div>
    <div class="name" style="position:absolute;top:5px;left:33px">Dr. Lena Marsh <span class="tick"></span></div>
    <div class="meta" style="position:absolute;top:11px;left:33px">✚ Orthopedic · ◉ 501m</div>
    <div class="tiny" style="position:absolute;top:16px;left:33px;width:53px;line-height:4.4px">Dr. Marsh is a genius in all arts of doctory. She's truely a m...</div>
    <div class="meta" style="position:absolute;top:28px;left:33px"><span class="stars">★★★★★</span> 4.5 · 1.2K</div>
    <div style="position:absolute;top:40px;left:4px;width:81px;height:7px;background:#eafbe4;border:.4px solid var(--green-bright);border-radius:2px;font-size:2.9px;line-height:6.4px;padding:0 2px" class="row"><span>Match with You</span><span style="color:var(--green)">99.571%</span></div>
  </div>
  <div class="sec" style="top:149px;left:4px;font-size:3.6px">Doctors Near You <span style="color:var(--muted);font-weight:400">(55)</span></div>
  <div class="card" style="top:158px;left:4px;width:89px;height:27px">
    <div class="avatar" role="img" aria-label="Doctor portrait" style="position:absolute;top:3px;left:3px;width:21px;height:21px"></div>
    <div class="name" style="position:absolute;top:4px;left:28px">Dr. Iris Dunn <span class="tick"></span></div>
    <div class="meta" style="position:absolute;top:10px;left:28px">Neurologist · ◉ 1.1km</div>
    <div class="meta" style="position:absolute;top:16px;left:28px"><span class="stars">★★★☆☆</span> 3.2 · 912</div>
  </div>
  <div class="card" style="top:189px;left:4px;width:89px;height:27px">
    <div class="avatar" role="img" aria-label="Doctor portrait" style="position:absolute;top:3px;left:3px;width:21px;height:21px"></div>
    <div class="name" style="position:absolute;top:4px;left:28px">Dr. Nora Kell</div>
    <div class="meta" style="position:absolute;top:10px;left:28px">Lung Specialist · ◉ 52m</div>
    <div class="meta" style="position:absolute;top:16px;left:28px"><span class="stars">★★★★☆</span> 4.2 · 157</div>
  </div>
  <div class="card" style="top:220px;left:0;width:66px;height:27px">
    <div class="name" style="position:absolute;top:4px;left:0">r. Mira Yates</div>
    <div class="meta" style="position:absolute;top:10px;left:0">Orthopedic · ◉ 803m</div>
    <div class="meta" style="position:absolute;top:16px;left:0"><span class="stars">★★☆☆☆</span> 2.8 · 998</div>
  </div>
  <div style="top:227px;left:68px;width:12px;height:12px;border-radius:3px;background:var(--peach)"></div>
  <div style="top:227px;left:82px;width:12px;height:12px;border-radius:3px;background:var(--dark)"></div>
  <div class="card" style="top:251px;left:4px;width:89px;height:27px">
    <div class="avatar" role="img" aria-label="Doctor portrait" style="position:absolute;top:3px;left:3px;width:21px;height:21px"></div>
    <div class="name" style="position:absolute;top:4px;left:28px">Dr. Iris Dunn <span class="tick"></span></div>
    <div class="meta" style="position:absolute;top:10px;left:28px">Neurologist · ◉ 4.6km</div>
    <div class="meta" style="position:absolute;top:16px;left:28px"><span class="stars">★★★★☆</span> 4.2 · 19</div>
  </div>
  <div class="nav" style="top:290px;left:4px;width:89px"><i class="on"></i><i></i><i></i><i></i><i></i></div>
</section>

<!-- Book doctor: time -->
<section class="screen book" style="left:604px;top:36px;height:421px">
  <div class="status">9:41</div><div class="status-icons"></div>
  <div class="back" style="top:16px;left:4px">‹</div>
  <div class="topbar-title" style="top:19px;left:0;width:97px;text-align:center">Book Doctor</div>
  <div class="back" style="top:16px;right:4px;left:auto">⚙</div>
  <svg style="top:36px;left:12px" width="73" height="5" viewBox="0 0 73 5"><line x1="3" y1="2.5" x2="70" y2="2.5" stroke="#f4c59a" stroke-width=".5" stroke-dasharray="1.5 1"/><circle cx="3" cy="2.5" r="2.3" fill="#fdcb9b"/><circle cx="36.5" cy="2.5" r="2.3" fill="#fdcb9b"/><circle cx="70" cy="2.5" r="2.3" fill="#eee"/></svg>
  <div class="row" style="top:44px;left:3px;width:91px;font-size:3.3px;font-weight:600"><span>Patient Detail</span><span>Time &amp; Date</span><span>Payment</span></div>
  <div class="card" style="top:59px;left:4px;width:89px;height:28px">
    <div class="avatar" role="img" aria-label="Doctor portrait" style="position:absolute;top:3px;left:3px;width:22px;height:22px"></div>
    <div class="name" style="position:absolute;top:5px;left:28px">Dr. Lena Marsh <span class="tick"></span></div>
    <div class="meta" style="position:absolute;top:11px;left:28px">Neurologist · ◉ 501m</div>
    <div class="meta" style="position:absolute;top:17px;left:28px"><span class="stars">★★★★★</span> 4.5 · 1.2K</div>
  </div>
  <div style="top:98px;left:4px;font-size:3.6px;font-weight:700">Select Date</div>
  <div class="meta" style="top:98px;right:4px">▣ <b style="color:var(--ink)">Mar 2026</b> ⌄</div>
  <div style="top:106px;left:3px;width:91px;display:grid;grid-template-columns:repeat(7,1fr);row-gap:6.2px;font-size:3.3px;text-align:center;font-weight:600">
    <span class="tiny">M</span><span class="tiny">T</span><span class="tiny">W</span><span class="tiny">T</span><span class="tiny">F</span><span class="tiny">S</span><span class="tiny">S</span>
    <span style="color:#ccc">29</span><span style="color:#ccc">30</span><span style="color:#ccc">31</span><span>1</span><span>2</span><span>3</span><span>4</span>
    <span>5</span><span>6</span><span>7</span><span>8</span><span>9</span><span>10</span><span>11</span>
    <span>12</span><span>13</span><span>14</span><span>15</span><span style="background:var(--peach);border-radius:2px;color:var(--orange-deep)">16</span><span>17</span><span>18</span>
    <span>19</span><span>20</span><span>21</span><span>22</span><span>23</span><span>24</span><span>25</span>
    <span>26</span><span>27</span><span>28</span><span>29</span><span>30</span><span style="color:#ccc">1</span><span style="color:#ccc">2</span>
  </div>
  <div style="top:187px;left:4px;width:89px;height:.4px;background:var(--line)"></div>
  <div style="top:194px;left:4px;font-size:3.6px;font-weight:700">Select Time</div>
  <div style="top:202px;left:3px;width:91px;display:grid;grid-template-columns:repeat(4,1fr);gap:3px;font-size:3.5px;text-align:center;font-weight:600">
    <span style="background:#f4f4f4;border-radius:2px;line-height:9px">08:00</span><span style="background:#f4f4f4;border-radius:2px;line-height:9px">09:00</span><span style="background:var(--dark);color:#fff;border-radius:2px;line-height:9px">10:00</span><span style="background:#f4f4f4;border-radius:2px;line-height:9px">11:00</span>
    <span style="background:#f4f4f4;border-radius:2px;line-height:9px">12:00</span><span style="background:#f4f4f4;border-radius:2px;line-height:9px">13:00</span><span style="background:#f4f4f4;border-radius:2px;line-height:9px">14:00</span><span style="background:#f4f4f4;border-radius:2px;line-height:9px">15:00</span>
  </div>
  <div style="top:243px;left:4px;font-size:3.6px;font-weight:700">Appointment Type</div>
  <div style="top:251px;left:4px;width:89px;height:11px;background:#f2f2f2;border-radius:3px">
    <div style="position:absolute;top:1px;left:1px;width:43px;height:9px;background:#fff;border-radius:2px;font-size:3.2px;font-weight:700;text-align:center;line-height:9px">In-Person</div>
    <div style="position:absolute;top:1px;right:1px;width:43px;height:9px;font-size:3.2px;color:var(--muted);text-align:center;line-height:9px">Video Call</div>
  </div>
  <div style="top:266px;left:4px;width:89px;height:23px;background:#fff2f3;border:.4px solid #f7a4ae;border-radius:3px;padding:3px 4px;font-size:3px;line-height:4.6px">
    <div style="color:var(--red);font-weight:600">▲ In-person visit currently unavailable</div>
    <div style="color:var(--muted);text-align:center">Due to high demand of in-person visit, we only offer video visit for now.</div>
  </div>
  <div style="top:308px;left:4px;font-size:3.6px;font-weight:700">Clinic Location</div>
  <div class="card" style="top:316px;left:4px;width:89px;height:64px">
    <div role="img" aria-label="Street map showing clinic location pins" style="position:absolute;top:3px;left:3px;width:83px;height:36px;border-radius:3px;background:linear-gradient(135deg,#f4f1ea,#fde9c9 50%,#dfe9f7)"></div>
    <div style="position:absolute;top:44px;left:4px;width:6px;height:6px;border-radius:50%;background:#ddd"></div>
    <div style="position:absolute;top:43px;left:16px;font-size:3.4px;font-weight:700">Brook Clinics 3, LTD</div>
    <div class="meta" style="position:absolute;top:49px;left:16px">501m · 18 Alder Street</div>
    <div style="position:absolute;top:55px;left:16px;font-size:2.9px;color:var(--orange-deep);font-weight:600">Show Direction</div>
  </div>
  <div class="btn-orange" style="top:391px;left:4px;width:89px;height:14px;line-height:14px;font-size:3.8px">Continue →</div>
  <div class="home-bar"></div>
</section>

<!-- Book doctor: payment -->
<section class="screen pay" style="left:722px;top:36px;height:265px">
  <div class="status">9:41</div><div class="status-icons"></div>
  <div class="back" style="top:16px;left:4px">‹</div>
  <div class="topbar-title" style="top:19px;left:0;width:97px;text-align:center">Book Doctor</div>
  <div class="back" style="top:16px;right:4px;left:auto">⚙</div>
  <svg style="top:36px;left:12px" width="73" height="5" viewBox="0 0 73 5"><line x1="3" y1="2.5" x2="70" y2="2.5" stroke="#f4c59a" stroke-width=".5" stroke-dasharray="1.5 1"/><circle cx="3" cy="2.5" r="2.3" fill="#fdcb9b"/><circle cx="36.5" cy="2.5" r="2.3" fill="#fdcb9b"/><circle cx="70" cy="2.5" r="2.3" fill="#f4a259"/></svg>
  <div class="row" style="top:44px;left:3px;width:91px;font-size:3.3px;font-weight:600"><span>Patient Detail</span><span>Time &amp; Date</span><span>Payment</span></div>
  <div class="card" style="top:59px;left:4px;width:89px;height:28px">
    <div class="avatar" role="img" aria-label="Doctor portrait" style="position:absolute;top:3px;left:3px;width:22px;height:22px"></div>
    <div class="name" style="position:absolute;top:5px;left:28px">Dr. Lena Marsh <span class="tick"></span></div>
    <div class="meta" style="position:absolute;top:11px;left:28px">Neurologist · ◉ 501m</div>
    <div class="meta" style="position:absolute;top:17px;left:28px"><span class="stars">★★★★★</span> 4.5 · 1.2K</div>
  </div>
  <div style="top:98px;left:4px;font-size:3.6px;font-weight:700">Promo Code</div>
  <div style="top:105px;left:4px;width:64px;height:13px;border:.4px solid var(--peach);border-radius:3px;font-size:3.4px;line-height:12px;padding-left:7px">2025KNRA</div>
  <div class="btn-orange" style="top:105px;left:71px;width:22px;height:13px;line-height:13px;font-size:3.4px">Use</div>
  <div style="top:121px;left:4px;width:89px;height:10px;background:#eef0fe;border:.4px solid #b7bff5;border-radius:3px;font-size:3px;line-height:9.5px;padding-left:4px;color:#4957c9">★ 50% OFF Coupon successfully applied!</div>
  <div style="top:142px;left:4px;font-size:3.6px;font-weight:700">Payment Detail</div>
  <div style="top:150px;left:4px;width:89px;font-size:3px;line-height:8.2px">
    <div class="row"><span style="color:var(--muted)">1x Consultation Package (30min)</span><span>$150.00</span></div>
    <div class="row"><span style="color:var(--muted)">Admin Fee</span><span>$10</span></div>
    <div class="row"><span style="color:var(--muted)">Coupon Discount</span><span>-$20</span></div>
  </div>
  <div style="top:179px;left:4px;width:89px;height:.4px;background:var(--line)"></div>
  <div class="row" style="top:181px;left:4px;width:89px;align-items:center"><span style="font-size:3.2px;color:var(--muted)">Grand Total</span><span style="font-size:6.4px;font-weight:800">$120.00</span></div>
  <div style="top:198px;left:4px;font-size:3.6px;font-weight:700">Payment Methods</div>
  <div class="card" style="top:206px;left:4px;width:89px;height:20px">
    <div style="position:absolute;top:5px;left:5px;font-size:7px;font-weight:800;color:var(--ink)">Paycard</div>
    <div style="position:absolute;top:4px;right:4px;width:12px;height:12px;border-radius:50%;background:#f4f4f4;font-size:4px;text-align:center;line-height:12px">⌄</div>
  </div>
  <div style="top:234px;left:4px;width:89px;height:19px;background:var(--dark);border-radius:5px">
    <div style="position:absolute;top:3px;left:4px;font-size:6px;font-weight:800;color:#fff">$87.52</div>
    <div style="position:absolute;top:12px;left:4px;font-size:2.8px;color:#ccc">Total Price</div>
    <div class="btn-orange" style="position:absolute;top:4px;right:3px;width:38px;height:11px;line-height:11px;font-size:3.4px">Checkout ▣</div>
  </div>
  <div class="home-bar"></div>
</section>

<!-- Appointments -->
<section class="screen appts" style="left:838px;top:36px;height:210px">
  <div class="status">9:41</div><div class="status-icons"></div>
  <div class="back" style="top:16px;left:4px">‹</div>
  <div class="topbar-title" style="top:19px;left:19px">My Appointments</div>
  <div style="top:33px;left:3px;display:flex;gap:2px;text-align:center">
    <div style="width:15px;height:20px;border:.4px solid var(--line);border-radius:3px;padding-top:2px"><div class="tiny">Mon</div><div style="font-size:5px;font-weight:700">11</div></div>
    <div style="width:15px;height:20px;border:.4px solid var(--line);border-radius:3px;padding-top:2px"><div class="tiny">Tue</div><div style="font-size:5px;font-weight:700">12</div></div>
    <div style="width:15px;height:20px;border:.6px solid var(--peach);border-radius:3px;padding-top:2px"><div class="tiny">Wed</div><div style="font-size:5px;font-weight:700">13</div></div>
    <div style="width:15px;height:20px;border:.4px solid var(--line);border-radius:3px;padding-top:2px"><div class="tiny">Thu</div><div style="font-size:5px;font-weight:700">14</div></div>
    <div style="width:15px;height:20px;border:.4px solid var(--line);border-radius:3px;padding-top:2px"><div class="tiny">Fri</div><div style="font-size:5px;font-weight:700">15</div></div>
    <div style="width:15px;height:20px;border:.4px solid var(--line);border-radius:3px;padding-top:2px"><div class="tiny">Sat</div><div style="font-size:5px;font-weight:700">16</div></div>
  </div>
  <div style="top:64px;left:4px;font-size:3.6px;font-weight:700" class="h">Upcoming Appointments</div>
  <div class="tiny" style="top:65px;right:4px">Newest First</div>
  <div class="tiny" style="top:88px;left:4px;text-align:center;color:var(--ink)">◷<br>11:00</div>
  <div class="card" style="top:73px;left:19px;width:75px;height:32px">
    <div class="avatar" role="img" aria-label="Doctor portrait" style="position:absolute;top:3px;left:3px;width:11px;height:11px"></div>
    <div class="name" style="position:absolute;top:3px;left:17px;font-size:3.4px">Dr. Lena Marsh</div>
    <div class="meta" style="position:absolute;top:9px;left:17px">Certified Cardiologist</div>
    <div style="position:absolute;top:16px;left:3px;width:69px;height:6px;background:#f5f5f5;border-radius:2px;font-size:2.6px;text-align:center;line-height:6px">General Health Checkup</div>
    <div class="meta" style="position:absolute;top:24px;left:3px">◷ 10:25 - 11:35 AM · ◉ $550</div>
  </div>
  <div class="card" style="top:110px;left:0;width:56px;height:32px">
    <div class="name" style="position:absolute;top:3px;left:6px;font-size:3.4px">Dr. Felix Rowe</div>
    <div class="meta" style="position:absolute;top:9px;left:6px">Certified Cardiologist</div>
    <div style="position:absolute;top:16px;left:2px;width:50px;height:6px;background:#f5f5f5;border-radius:2px;font-size:2.6px;text-align:center;line-height:6px">General Health Checkup</div>
    <div class="meta" style="position:absolute;top:24px;left:0">25 - 11:35 AM · ◉ $550</div>
  </div>
  <div style="top:118px;left:58px;width:13px;height:13px;border-radius:3px;background:var(--peach)"></div>
  <div style="top:118px;left:74px;width:13px;height:13px;border-radius:3px;background:var(--red);color:#fff;font-size:6px;text-align:center;line-height:13px">×</div>
  <div class="tiny" style="top:165px;left:4px;text-align:center;color:var(--ink)">◷<br>12:00</div>
  <div class="card" style="top:151px;left:19px;width:75px;height:32px">
    <div class="avatar" role="img" aria-label="Doctor portrait" style="position:absolute;top:3px;left:3px;width:11px;height:11px"></div>
    <div class="name" style="position:absolute;top:3px;left:17px;font-size:3.4px">Dr. Lena Marsh</div>
    <div class="meta" style="position:absolute;top:9px;left:17px">Certified Cardiologist</div>
    <div style="position:absolute;top:16px;left:3px;width:69px;height:6px;background:#f5f5f5;border-radius:2px;font-size:2.6px;text-align:center;line-height:6px">General Health Checkup</div>
    <div class="meta" style="position:absolute;top:24px;left:3px">◷ 10:25 - 11:35 AM · ◉ $550</div>
  </div>
  <div class="card" style="top:190px;left:19px;width:75px;height:24px">
    <div class="avatar" role="img" aria-label="Doctor portrait" style="position:absolute;top:3px;left:3px;width:11px;height:11px"></div>
    <div class="name" style="position:absolute;top:3px;left:17px;font-size:3.4px">Dr. Felix Rowe</div>
    <div class="meta" style="position:absolute;top:9px;left:17px">Certified Cardiologist</div>
  </div>
</section>

<!-- Video call -->
<section class="screen call" style="left:956px;top:36px;height:210px;background:var(--dark)">
  <div role="img" aria-label="Video feed of Dr. Lena Marsh in white coat" style="top:0;left:0;width:97px;height:175px;background:linear-gradient(170deg,#e9e7e5,#cac4bf 55%,#a9a29c)"></div>
  <div class="status">9:41</div>
  <div style="top:19px;right:5px;background:var(--red);color:#fff;font-size:3.6px;font-weight:700;padding:1.5px 3px;border-radius:3px">◉ 05:24</div>
  <div style="top:48px;left:9px;width:1.6px;height:50px;background:rgba(255,255,255,.6);border-radius:1px"></div>
  <div style="top:155px;left:4px;font-size:5.6px;font-weight:800;color:#2d3436">Dr. Lena Marsh</div>
  <div style="top:165px;left:4px;font-size:3.4px;color:#4a4f52">Certified Neurolist</div>
  <div role="img" aria-label="Self view of patient" style="top:139px;left:68px;width:25px;height:32px;border-radius:4px;background:linear-gradient(160deg,#c9b6a8,#7c675a);border:.8px solid #fff"></div>
  <div style="top:182px;left:17px;width:14px;height:14px;border-radius:50%;background:#4a5254"></div>
  <div style="top:180px;left:38px;width:20px;height:18px;border-radius:6px;background:var(--red);color:#fff;text-align:center;line-height:18px;font-size:7px">✆</div>
  <div style="top:182px;left:65px;width:14px;height:14px;border-radius:50%;background:#4a5254"></div>
  <div class="home-bar" style="background:#fff"></div>
</section>

<!-- Chat -->
<section class="screen chat" style="left:1073px;top:36px;height:210px">
  <div class="status">9:41</div><div class="status-icons"></div>
  <div class="back" style="top:16px;left:4px">‹</div>
  <div style="top:16px;left:17px;font-size:4px;font-weight:700">Dr. Lena Marsh</div>
  <div class="tiny" style="top:22px;left:17px">Certified Neurolist</div>
  <div style="top:17px;right:5px;font-size:5px">⌕</div>
  <div style="top:38px;left:4px;width:89px;height:80px;background:var(--peach);border-radius:5px">
    <div style="position:absolute;top:4px;left:4px;width:66px;font-size:2.9px;line-height:4.4px;color:#7a4a1f">Hi doc, my leg hurts, can you check and see what's the problem is? It hurts so much!</div>
    <div style="position:absolute;top:4px;right:4px;width:9px;height:9px;border-radius:50%;background:var(--orange-deep)"></div>
    <div role="img" aria-label="Photo of injured leg" style="position:absolute;top:21px;left:4px;width:70px;height:42px;border-radius:3px;background:linear-gradient(160deg,#efe7e1,#c9bab0)"></div>
    <div style="position:absolute;top:65px;left:4px;width:70px;height:9px;background:#fff;border-radius:2px;font-size:2.6px;line-height:9px;padding-left:2px">leg_hurts-so-much.jpg</div>
  </div>
  <div style="top:122px;left:4px;width:89px;height:20px;background:#f4f4f4;border-radius:5px">
    <div style="position:absolute;top:5px;left:4px;width:7px;height:7px;border-radius:50%;background:#ddd"></div>
    <div style="position:absolute;top:3px;left:15px;width:70px;font-size:2.8px;line-height:4.3px;color:#555">Hi Elsa, that's a symptom for <b>Rheumatoid Arthritis</b>. It's common among the most common causes.</div>
  </div>
  <div class="tiny" style="top:148px;left:0;width:97px;text-align:center">Today at 12:12 AM</div>
  <div style="top:156px;left:4px;width:89px;height:15px;background:var(--peach-soft);border-radius:4px">
    <div style="position:absolute;top:3px;left:4px;font-size:2.9px;line-height:4.3px;color:var(--orange-deep)">What! Sounds scary!<br>What should I do?</div>
    <div style="position:absolute;top:3px;right:4px;width:9px;height:9px;border-radius:50%;background:var(--orange-deep)"></div>
  </div>
  <div style="top:189px;left:4px;width:89px;height:13px;background:var(--dark);border-radius:4px">
    <div style="position:absolute;top:4.5px;left:5px;font-size:2.9px;color:#fff">◉ OMG, TYSM Doctor!|</div>
    <div style="position:absolute;top:2px;right:2px;width:9px;height:9px;border-radius:3px;background:#fff;font-size:4px;text-align:center;line-height:9px">↵</div>
  </div>
</section>

<!-- Home preview (large) -->
<section class="screen home-preview" style="left:864px;top:283px;width:122px;height:300px;border-radius:14px">
  <div style="top:20px;left:8px;font-size:3.4px;font-weight:700;color:var(--muted)">▣ SAT, 25 JUN 2026</div>
  <div style="top:20px;right:10px;width:5px;height:5px;border-radius:50%;background:var(--red)"></div>
  <div class="avatar" role="img" aria-label="User portrait" style="top:33px;left:8px;width:16px;height:16px;border-radius:50%"></div>
  <div style="top:33px;left:28px;font-size:7px;font-weight:800">Hello, Elsa!</div>
  <div style="top:43px;left:28px;font-size:3.6px;color:var(--muted)"><span style="color:var(--green-bright)">✚</span> 94% Healthy · <span style="color:var(--star)">★</span> Pro Member</div>
  <div style="top:36px;right:8px;font-size:6px">›</div>
  <div class="sec" style="top:74px;left:6px;font-size:5px">Quick Health Summary</div>
  <div style="top:85px;left:6px;width:48px;height:63px;background:var(--green);border-radius:6px">
    <div style="position:absolute;top:5px;left:5px;font-size:3.8px;font-weight:700;color:#fff">Heart Rate</div>
    <div style="position:absolute;top:12px;left:5px;font-size:7.5px;font-weight:800;color:#fff">96 <span style="font-size:3.8px">bpm</span></div>
    <svg style="position:absolute;top:28px;left:3px" width="42" height="32" viewBox="0 0 36 26"><path d="M1 24 C6 10,8 8,11 20 S16 2,19 14 S24 20,27 6 S32 10,35 4" fill="none" stroke="#7ed957" stroke-width="1.6"/></svg>
  </div>
  <div style="top:85px;left:58px;width:48px;height:63px;background:var(--red);border-radius:6px">
    <div style="position:absolute;top:5px;left:5px;font-size:3.8px;font-weight:700;color:#fff">Steps Taken</div>
    <div style="position:absolute;top:12px;left:5px;font-size:7.5px;font-weight:800;color:#fff">1578 <span style="font-size:3.8px">total</span></div>
    <svg style="position:absolute;top:28px;left:5px" width="38" height="32" viewBox="0 0 32 26"><g fill="#ff9aa6"><rect x="1" y="16" width="3" height="10" rx="1.5"/><rect x="6" y="10" width="3" height="16" rx="1.5"/><rect x="11" y="4" width="3" height="22" rx="1.5" fill="#fff"/><rect x="16" y="12" width="3" height="14" rx="1.5"/><rect x="21" y="18" width="3" height="8" rx="1.5"/><rect x="26" y="21" width="3" height="5" rx="1.5"/></g></svg>
  </div>
  <div style="top:85px;left:110px;width:14px;height:63px;background:var(--blue);border-radius:6px"></div>
  <div class="sec" style="top:163px;left:6px;font-size:5px">Virtual Consultations</div>
  <div style="top:176px;left:8px;font-size:11px;font-weight:800">89+</div>
  <div style="top:190px;left:8px;font-size:3.6px;color:var(--muted)">List Consultations</div>
  <div style="top:177px;right:12px;width:11px;height:11px;border:.5px solid #ddd;border-radius:3px;text-align:center;line-height:10.5px;font-size:7px;color:var(--muted)">+</div>
  <div class="avatar" role="img" aria-label="Doctor portrait" style="top:210px;left:10px;width:18px;height:20px"></div>
  <div style="top:211px;left:33px;font-size:4.6px;font-weight:700">Dr. Clara Voss</div>
  <div class="meta" style="top:219px;left:33px;font-size:3.4px"><span class="stars">★</span> 4.1 · Cardiologist</div>
  <div class="meta" style="top:225px;left:33px;font-size:3.4px">● 15:25 PM - 17:25 PM</div>
  <div class="avatar" role="img" aria-label="Doctor portrait" style="top:246px;left:10px;width:18px;height:20px"></div>
  <div style="top:247px;left:33px;font-size:4.6px;font-weight:700">Dr. Owen Hale</div>
  <div class="meta" style="top:255px;left:33px;font-size:3.4px"><span class="stars">★</span> 4.6 · Orthopedics</div>
  <div class="meta" style="top:261px;left:33px;font-size:3.4px">● 9:25 AM - 11:25 AM</div>
</section>

<!-- Video call preview (large) -->
<section class="screen call-preview" style="left:994px;top:357px;width:134px;height:280px;border-radius:16px;background:var(--dark)">
  <div role="img" aria-label="Video feed of Dr. Lena Marsh in white coat" style="top:0;left:0;width:134px;height:230px;background:linear-gradient(170deg,#e9e7e5,#cac4bf 55%,#a9a29c)"></div>
  <div class="status" style="top:9px;left:12px;font-size:5px">9:41</div>
  <div class="status-icons" style="top:10px;right:12px;width:16px;height:4px"></div>
  <div style="top:30px;right:8px;background:var(--red);color:#fff;font-size:5px;font-weight:700;padding:2px 4px;border-radius:4px">◉ 05:24</div>
  <div style="top:65px;left:12px;width:2px;height:70px;background:rgba(255,255,255,.6);border-radius:1px"></div>
  <div style="top:202px;left:6px;font-size:8px;font-weight:800;color:#2d3436">Dr. Lena Marsh</div>
  <div style="top:216px;left:6px;font-size:4.8px;color:#4a4f52">Certified Neurolist</div>
  <div role="img" aria-label="Self view of patient" style="top:180px;left:96px;width:33px;height:42px;border-radius:5px;background:linear-gradient(160deg,#c9b6a8,#7c675a);border:1px solid #fff"></div>
  <div style="top:241px;left:22px;width:20px;height:20px;border-radius:50%;background:#4a5254"></div>
  <div style="top:238px;left:53px;width:28px;height:26px;border-radius:8px;background:var(--red);color:#fff;text-align:center;line-height:26px;font-size:10px">✆</div>
  <div style="top:241px;left:92px;width:20px;height:20px;border-radius:50%;background:#4a5254"></div>
  <div class="home-bar" style="background:#fff;bottom:4px"></div>
</section>

</body>
</html>
```